business card for LWR pty ltd

We require a business card that stands out . I have included our company flyer and would like the services listed to be put on the card so when we Give out the cards to customers they have an idea of services we provide. need the winning design to be in editable photo shop format, editable iMac pages format or editable windows publisher format, so that I can enter in names, email addresses, phone numbers etc myself. I have included a pdf documents of info / items needed on the card to use as reference please.
Updates

need more submissions

Need extra days to review

Sick

Target Market(s)

new customers

Contact Information for Business Card

details are on attached business card requirements file

Requirements
Must have
• I have attached a list of must haves

```html
<!DOCTYPE html>
<html lang="en">
<head>
<meta charset="utf-8">
<title>LWR Pty Ltd — Business Card</title>
<link rel="stylesheet" href="https://fonts.googleapis.com/css2?family=Lato:wght@300;400;700;900&display=swap">
<style>
  :root {
    --backdrop: #3a3b3e;
    --card: #050505;
    --ink: #ffffff;
    --muted: #b9b9b9;
    --rule: #d9d9d9;
    --mesh-top: #2e2f33;
    --mesh-bottom: #070708;
    --dirt: #9a6a3e;
    --dirt-dark: #4a3220;
    --truck: #1e2226;
    --tank: #c9c6bc;
  }
  * { box-sizing: border-box; margin: 0; padding: 0; }
  html, body { width: 1200px; height: 900px; overflow: hidden; }
  body {
    background: var(--backdrop);
    font-family: "Lato", sans-serif;
    color: var(--ink);
    position: relative;
  }
  .card {
    position: absolute;
    width: 700px;
    height: 400px;
    background: var(--card);
    border-radius: 18px;
    overflow: hidden;
  }
  .card--front { left: 70px; top: 45px; }
  .card--back  { left: 430px; top: 465px; }

  /* Front */
  .front-mesh {
    position: absolute; inset: 0;
    background: radial-gradient(ellipse 70% 55% at 55% 25%, var(--mesh-top), var(--mesh-bottom) 80%);
  }
  .front-photo {
    position: absolute; left: 150px; top: 150px; width: 550px; height: 172px;
    background: linear-gradient(160deg, var(--dirt-dark) 0%, var(--dirt) 45%, var(--truck) 100%);
  }
  .brand {
    position: absolute; left: 0; right: 0; top: 34px;
    text-align: center;
    font-weight: 900; font-size: 110px; letter-spacing: 6px;
    color: var(--ink); line-height: 1;
    z-index: 1;
  }
  .services {
    position: absolute; left: 20px; right: 20px; top: 332px;
    text-align: center; font-size: 13px; line-height: 1.38; font-weight: 400;
  }

  /* Back */
  .truck-photo {
    position: absolute;
    border-radius: 6px;
  }
  .truck-photo--top  { left: 380px; top: 55px; width: 280px; height: 88px;
    background: linear-gradient(100deg, var(--truck) 0%, #3b4148 45%, var(--tank) 100%); }
  .truck-photo--left { left: 60px; top: 150px; width: 222px; height: 80px;
    background: linear-gradient(280deg, var(--truck) 0%, #3b4148 45%, var(--tank) 100%); }

  .person__name {
    position: absolute; left: 290px; width: 250px; top: 190px;
    text-align: center; font-weight: 900; font-size: 30px; line-height: 36px;
  }
  .person__role {
    position: absolute; left: 290px; width: 250px; top: 240px;
    text-align: center; font-weight: 300; font-size: 17px; color: var(--muted);
  }

  .rule { position: absolute; height: 1px; background: var(--rule); }
  .rule--main { left: 290px; right: 35px; top: 232px; }
  .rule--contact { left: 130px; width: 280px; top: 300px; }

  .company {
    position: absolute; right: 40px; top: 242px; text-align: right;
    font-style: normal; font-weight: 300; font-size: 17px; line-height: 1.3;
  }
  .contact {
    position: absolute; left: 130px; top: 310px; list-style: none;
    font-weight: 300; font-size: 17px;
  }
  .contact li { display: flex; align-items: center; gap: 12px; height: 25px; }
  .contact svg { width: 16px; height: 16px; flex: none; }
</style>
</head>
<body>
  <section class="card card--front">
    <div class="front-mesh" role="img" aria-label="Dark metallic hexagonal mesh texture"></div>
    <div class="front-photo" role="img" aria-label="Photograph of a road train tipper truck on a red dirt outback road"></div>
    <div class="brand">LWR</div>
    <p class="services">
      Over size loads/Hot shot loads | Heavy vehicle recovery services | Portable water deliveries<br>
      Road building/Maintenance | Earthworks | Sand &amp; metal supply &amp; cartage | Road train tippers<br>
      Road train tankers | Road train flat tops | Drop deck trailers | Mine site accredited equipment &amp; operators
    </p>
  </section>

  <section class="card card--back">
    <div class="truck-photo truck-photo--top" role="img" aria-label="Photograph of a road train tanker truck"></div>
    <div class="truck-photo truck-photo--left" role="img" aria-label="Photograph of a road train tanker truck facing left"></div>

    <div class="person__name">Daniel Harker</div>
    <div class="rule rule--main"></div>
    <div class="person__role">Director</div>

    <address class="company">
      LWR Pty Ltd<br>
      Lot 114, Ninemile Track<br>
      Redgum Flat, Australia
    </address>

    <div class="rule rule--contact"></div>
    <ul class="contact">
      <li>
        <svg viewBox="0 0 24 24" aria-hidden="true"><path fill="#fff" d="M6.6 10.8a15 15 0 0 0 6.6 6.6l2.2-2.2c.3-.3.7-.4 1-.2 1.1.4 2.3.6 3.6.6.6 0 1 .4 1 1V20c0 .6-.4 1-1 1A17 17 0 0 1 3 4c0-.6.4-1 1-1h3.5c.6 0 1 .4 1 1 0 1.3.2 2.5.6 3.6.1.3 0 .7-.2 1z"/></svg>
        000 555 0100
      </li>
      <li>
        <svg viewBox="0 0 24 24" aria-hidden="true"><rect x="2" y="5" width="20" height="14" fill="#fff"/><path d="M2 5l10 8 10-8" fill="none" stroke="#050505" stroke-width="1.6"/></svg>
        info@lwrservices.com.au
      </li>
      <li>
        <svg viewBox="0 0 24 24" aria-hidden="true"><circle cx="12" cy="12" r="9.5" fill="none" stroke="#fff" stroke-width="1.8"/><path d="M2.5 12h19M12 2.5c3 3 3 16 0 19M12 2.5c-3 3-3 16 0 19" fill="none" stroke="#fff" stroke-width="1.4"/></svg>
        www.lwrservices.com.au
      </li>
    </ul>
  </section>
</body>
</html>
```